General contractor/GM consaltant business card

I need a card for my contracting company in North Dakota, we build industrial buildings for the oil feild and oil feild related companies offices, shops, airplain hangars, airports ext. We have a familly atmosphere on the job and are very relational and personal.
Industry/Entity Type
Industrial
Contact Information for Business Card
Kestrelmoor Builders LLC.
Dwight T.Halvorsun
4736 Quillfern dr. Colorado Springs, CO. 80927
Cell# 406-555-8142
dwight@kestrelmoorbuilders.com

```html
<!DOCTYPE html>
<html lang="en">
<head>
<meta charset="utf-8">
<title>Kestrelmoor Builders LLC – Business Card</title>
<link rel="stylesheet" href="https://fonts.googleapis.com/css2?family=Arimo:wght@400;700&display=swap">
<style>
  :root {
    --backdrop: #d9d9d9;
    --orange: #f7a11c;
    --ink: #111111;
    --white: #ffffff;
    --dark-top: #5a5a5a;
    --dark-bottom: #0b0b0b;
    --photo-light: #f2f2f2;
    --photo-mid: #a9a9a9;
    --photo-dark: #3c3c3c;
  }
  * { box-sizing: border-box; margin: 0; padding: 0; }
  html, body {
    width: 1200px; height: 900px; overflow: hidden;
    background: var(--backdrop);
    font-family: "Arimo", Arial, sans-serif;
  }
  .stage { position: relative; width: 1200px; height: 900px; }

  .card {
    position: absolute; left: 240px; width: 720px; height: 412px;
    overflow: hidden;
    box-shadow: 0 8px 24px rgba(0,0,0,.25);
  }
  .card--back { top: 30px; }
  .card--front { top: 458px; }

  /* Back side */
  .back__brand-band {
    position: absolute; left: 0; top: 0; width: 100%; height: 236px;
    background: var(--orange);
  }
  .back__divider {
    position: absolute; left: 0; top: 236px; width: 100%; height: 5px;
    background: var(--white);
  }
  .back__contact-band {
    position: absolute; left: 0; top: 241px; width: 100%; height: 171px;
    background: linear-gradient(160deg, var(--dark-top) 0%, #2a2a2a 45%, var(--dark-bottom) 100%);
  }
  .company-name {
    position: absolute; left: 30px; top: 24px;
    font-size: 31px; font-weight: 400; color: var(--ink);
  }
  .company-web {
    position: absolute; left: 30px; top: 64px;
    font-size: 19px; color: var(--ink);
  }
  .person {
    position: absolute; right: 30px; top: 156px; text-align: right; color: var(--ink);
  }
  .person__name { font-size: 29px; font-weight: 400; }
  .person__title { font-size: 18px; margin-top: 4px; margin-right: 46px; }

  .contact-list {
    position: absolute; left: 26px; top: 18px; list-style: none;
    color: var(--white); font-size: 14px; line-height: 1.3;
  }
  .contact-list li { display: flex; align-items: flex-start; gap: 10px; margin-bottom: 7px; }
  .contact-list svg { flex: none; width: 14px; height: 14px; margin-top: 1px; }

  /* Front side */
  .front__photo {
    position: absolute; inset: 0;
    background:
      radial-gradient(ellipse at 40% 30%, var(--photo-light) 0%, rgba(242,242,242,0) 55%),
      linear-gradient(180deg, var(--photo-mid) 0%, #cfcfcf 35%, var(--photo-dark) 55%, #e8e8e8 70%, var(--photo-light) 100%);
  }
  .front__title {
    position: absolute; left: 30px; top: 26px;
    font-size: 60px; font-weight: 400; color: rgba(255,255,255,.9);
    white-space: nowrap;
  }
</style>
</head>
<body>
<main class="stage">
  <section class="card card--back" aria-label="Business card back">
    <div class="back__brand-band">
      <p class="company-name">Kestrelmoor Builders LLC</p>
      <p class="company-web">www.kestrelmoorbuilders.com</p>
      <div class="person">
        <p class="person__name">Dwight T.Halvorsun</p>
        <p class="person__title">Founder</p>
      </div>
    </div>
    <div class="back__divider"></div>
    <div class="back__contact-band">
      <ul class="contact-list">
        <li>
          <svg viewBox="0 0 14 14" aria-hidden="true"><path d="M7 0.5a4.5 4.5 0 0 0-4.5 4.5c0 3.2 4.5 8.5 4.5 8.5s4.5-5.3 4.5-8.5A4.5 4.5 0 0 0 7 0.5z" fill="#fff"/><circle cx="7" cy="5" r="1.7" fill="#333"/></svg>
          <span>4736 Quillfern dr. Colorado Springs,<br>CO. 80927</span>
        </li>
        <li>
          <svg viewBox="0 0 14 14" aria-hidden="true"><rect x="3.5" y="1" width="7" height="12" rx="1" fill="none" stroke="#fff" stroke-width="1.2"/><line x1="6" y1="11" x2="8" y2="11" stroke="#fff" stroke-width="1"/></svg>
          <span>406-555-8142</span>
        </li>
        <li>
          <svg viewBox="0 0 14 14" aria-hidden="true"><rect x="1" y="3" width="12" height="8" fill="none" stroke="#fff" stroke-width="1.2"/><polyline points="1,3 7,8 13,3" fill="none" stroke="#fff" stroke-width="1.2"/></svg>
          <span>dwight@kestrelmoorbuilders.com</span>
        </li>
      </ul>
    </div>
  </section>

  <section class="card card--front" aria-label="Business card front">
    <div class="front__photo" role="img" aria-label="Black and white photo of two construction workers in hard hats, silhouetted against a city skyline and a crane on a building site"></div>
    <p class="front__title">Kestrelmoor Builders LLC</p>
  </section>
</main>
</body>
</html>
```